I am starting a company that will help small businesses that are looking to raise money over the internet (i.e. crowd fund) in reliance of the JOBS Act and the new rules that have been recently passed.

Initially, the website will help a business figure out if it is qualified to raise money and if so, it will tell the business what information is required.

The various pages will need to gather information from the businesses through Yes/No questionnaires, drop-down lists and free text boxes -

I am still thinking about my company's name and don't have a logo - for now, please use the name "RPMH (raise path mentor hub)" - feel free to throw in an idea for a logo

Hi all - I was wondering if I could get some design suggestions that don't use stock photos- thanks

Based on the designs I have received so far, I don't think the description of my website is clear.  The website will NOT be a crowdfunding portal (i.e. it is not like boostwell etc.)  It is an information website that will allow companies to determine if they are legally able to raise money online. 

If they are able to raise money online, then the company can sign-up for some paid services which include legal documents and agreements.

To help the design process, I've uploaded a draft of the questions that a company will need to answer to determine if it is able to raise money online.

The submitted designs should be for both the homepage as well as the pages on which the questions will be set out.

Thanks for taking the time to read.

small businesses that will be looking to raise money through crowd funding

Internet

• I need designs for the following pages:

1. Home page
- should be simple - links to 'about' page and 'blog' page
- room at the bottom for affiliate links/logos
- convey the message that there are many rules that need to be followed to legally crowd fund a company but that this website makes compliance easy
- prominent 'get started' button

2. Company questions pages
- laid out to ask ~ 5 questions:
- name of company (free text answer)
- amount raised in prior 12 months (drop down box)
- state of formation (drop down box)
- registered with the NRB (y/n)
- registered as an investment company (y/n)

- needs to be a help 'icon' beside the questions so that user can hover over the icon and get more information as to what the question is asking

3. Eligibility questions page
- list of ~25 questions (y/n) answers
-
4. Fund raising objectives page
- list of ~15 questions answers
- answers will be y/n, multiple choice, drop down menu or free text

5. Results page
- if company is not-eligible to proceed, display "Not Eligible" page with list of reasons why
- if company is eligible, display "Congratulations" page with link to "Sign-up and Continue"

6. Sign-up page
- name
- address
- e-mail etc.
- check box to agree to terms and conditions

7. 'blog' page

8. about / disclaimer page

```html
<!DOCTYPE html>
<html lang="en">
<head>
<meta charset="utf-8">
<title>RPMH — Making Crowd Fund Compliance Easy</title>
<link rel="stylesheet" href="https://fonts.googleapis.com/css2?family=Open+Sans:wght@300;400;600;700&family=Yanone+Kaffeesatz:wght@300;400;500;700&display=swap">
<style>
  :root {
    --green: #89d424;
    --green-soft: #a6e05a;
    --charcoal: #454545;
    --charcoal-dark: #2f2f2f;
    --white: #ffffff;
    --text: #7d7d7d;
    --date: #5a5a5a;
    --rule: #c9c9c9;
  }
  * { box-sizing: border-box; margin: 0; padding: 0; }
  html, body { width: 1200px; height: 973px; overflow: hidden; background: var(--white); }
  body { font-family: "Open Sans", Arial, sans-serif; position: relative; }

  .topbar { height: 60px; background: var(--charcoal); position: relative; }
  .brand {
    position: absolute; left: 120px; top: 0; width: 70px; height: 60px;
    background: #333333; border-top: 4px solid var(--green);
    color: var(--white); font-family: "Yanone Kaffeesatz", sans-serif; font-weight: 400;
    font-size: 30px; line-height: 52px; text-align: center; letter-spacing: 0.5px; text-decoration: none;
  }
  .main-nav { position: absolute; left: 240px; top: 0; display: flex; gap: 50px; }
  .main-nav a { color: var(--white); text-decoration: none; font-size: 14px; line-height: 61px; }
  .account { position: absolute; right: 130px; top: 0; line-height: 66px; font-family: Arial, Helvetica, sans-serif; font-size: 12px; color: var(--white); }
  .account a { color: var(--green); font-weight: bold; text-decoration: none; margin-left: 4px; }

  .hero { height: 418px; background: var(--green); position: relative; }
  .hero-visual {
    position: absolute; left: 188px; top: 43px; width: 342px; height: 342px; border-radius: 50%;
    background: radial-gradient(circle at 50% 50%, var(--green-soft) 0%, var(--green) 75%);
  }
  .hero-copy { position: absolute; left: 607px; top: 118px; color: var(--white); }
  .hero-title { font-family: "Yanone Kaffeesatz", sans-serif; text-transform: uppercase; line-height: 53px; }
  .hero-title .light { display: block; font-weight: 300; font-size: 60px; letter-spacing: 1.2px; }
  .hero-title .bold { display: block; font-weight: 700; font-size: 61px; letter-spacing: 3px; }
  .hero-tagline { font-weight: 300; font-size: 24px; margin-top: -2px; margin-left: 2px; }
  .btn-start {
    display: inline-flex; align-items: center; gap: 8px; margin-top: 30px;
    height: 43px; padding: 0 16px 0 17px; background: var(--charcoal); border-bottom: 3px solid var(--charcoal-dark);
    color: var(--white); font-weight: 700; font-size: 14px; text-decoration: none; text-transform: uppercase;
  }

  .content { display: flex; padding-left: 129px; gap: 23px; }
  .column { width: 459px; }
  .section-head { display: flex; align-items: center; gap: 15px; height: 103px; padding-top: 42px; border-bottom: 1px solid var(--rule); padding-left: 2px; }
  .section-head h2 { font-family: "Yanone Kaffeesatz", sans-serif; font-weight: 400; font-size: 31px; color: var(--green); }
  .about p { font-size: 14px; line-height: 22px; color: var(--text); padding-left: 2px; margin-top: 12px; }
  .about p + p { margin-top: 22px; }
  .more { display: inline-block; font-family: "Yanone Kaffeesatz", sans-serif; font-style: italic; font-size: 19px; color: var(--green); text-decoration: none; }
  .about .more { margin-top: 22px; padding-left: 2px; }
  .post { padding-left: 1px; }
  .post:first-of-type { margin-top: 28px; }
  .post + .post { margin-top: 24px; }
  .post:nth-of-type(3) { margin-top: 40px; }
  .post time { display: block; font-size: 12px; font-weight: 700; color: var(--date); line-height: 18px; }
  .post p { font-size: 14px; line-height: 22px; color: var(--text); margin-top: 6px; }
  .post .more { margin-top: 7px; line-height: 22px; }
</style>
</head>
<body>
  <header class="topbar">
    <a class="brand" href="#">RPMH</a>
    <nav class="main-nav">
      <a href="#">About</a>
      <a href="#">Blog</a>
      <a href="#">Get Started</a>
    </nav>
    <div class="account">Have an account? <a href="#">Sign In</a></div>
  </header>

  <section class="hero">
    <div class="hero-visual" role="img" aria-label="Large white checkmark inside a circle illustration"></div>
    <div class="hero-copy">
      <h1 class="hero-title"><span class="light">Making Crowd Fund</span><span class="bold">Compliance Easy</span></h1>
      <p class="hero-tagline">Another sentence that describe your site</p>
      <a class="btn-start" href="#">Get Started
        <svg width="9" height="12" viewBox="0 0 9 12" aria-hidden="true"><polyline points="2,1.5 7,6 2,10.5" fill="none" stroke="#fff" stroke-width="2.4"/></svg>
      </a>
    </div>
  </section>

  <main class="content">
    <section class="column about">
      <div class="section-head">
        <svg width="33" height="33" viewBox="0 0 33 33" aria-hidden="true">
          <circle cx="16.5" cy="16.5" r="15" fill="none" stroke="#89d424" stroke-width="2"/>
          <circle cx="16.5" cy="9.5" r="1.8" fill="#89d424"/>
          <path d="M13 14 h4.5 v10 M13 24.5 h7.5" fill="none" stroke="#89d424" stroke-width="2"/>
        </svg>
        <h2>A Few Words About</h2>
      </div>
      <p>Lorem ipsum dolor sit amet, consectetur adipiscing elit. Fusce at sollicitudin velit, vitae tristique nibh. Pellentesque nec ante vitae tellus porta dignissim. Interdum et malesuada fames ac ante ipsum primis in faucibus. Ut eu commodo diam</p>
      <p>Nam sollicitudin ut mauris eget fringilla. Donec et lectus id arcu scelerisque tincidunt. Donec nec sem vitae tortor hendrerit ultrices. Etiam dictum aliquet nunc sed gravida. Nam gravida, sem at facilisis tincidunt, lorem sem consectetur elit, in pharetra nisi neque sed urna. Mauris vehicula varius commodo. Pellentesque laoreet hendrerit libero at cursus.</p>
      <a class="more" href="#">About Us ›</a>
    </section>

    <section class="column blog">
      <div class="section-head">
        <svg width="34" height="32" viewBox="0 0 34 32" aria-hidden="true">
          <path d="M17 5 L17 30 M2 3 L17 5 L32 3 L32 28 L17 30 L2 28 Z" fill="none" stroke="#89d424" stroke-width="2" stroke-linejoin="round"/>
          <path d="M6 9 H13 M6 13 H13 M6 17 H13 M6 21 H13 M21 9 H28 M21 13 H28 M21 17 H28 M21 21 H28" stroke="#89d424" stroke-width="1.8"/>
        </svg>
        <h2>Latest Blog Posts</h2>
      </div>
      <article class="post">
        <time>Januar 01, 2014</time>
        <p>Lorem ipsum dolor sit amet, consectetur adipiscing elit. Fusce at sollicitudin velit, vitae tristique nibh...</p>
        <a class="more" href="#">Read More ›</a>
      </article>
      <article class="post">
        <time>Januar 01, 2014</time>
        <p>Lorem ipsum dolor sit amet, consectetur adipiscing elit. Fusce at sollicitudin velit, vitae tristique nibh...</p>
        <a class="more" href="#">Read More ›</a>
      </article>
      <article class="post">
        <time>Januar 01, 2014</time>
        <p>Lorem ipsum dolor sit amet, consectetur adipiscing elit. Fusce at sollicitudin velit, vitae tristique nibh...</p>
        <a class="more" href="#">Read More ›</a>
      </article>
    </section>
  </main>
</body>
</html>
```